Website Wordpress Responsive Design and Development - Landscape Company

Site is currently under construction, but the old site needs a refresh.
Need a fully responsive wordpress website (built in Elementor or comparable theme).
Here's the way it looked prior :
https://oldpages.example/snap/20220330041341/http://tobbsmaplegrove.example/
Their current designer came up with a website sample and it looks terrible :
https://danwelkerimages.sitebuild.example/mysite/projects
Websites the client likes for some inspiration, but needs better than these :
https://www.corwentlandscapearchitects.example/
http://qvateliernj.example/
https://brackenpartners.example/
https://www.tallanbysinc.example/

Navigation includes :
• Home
• Complete structure of website content is available in the home page, yielding main information on services.
• Visually appealing but simple to use and navigate. Subtle amount of content, but enough for search engines to be able to read up the target phrases.
• Sections on the home page include :
▪ About - Information about the company and main service focus
▪ Gallery - Imagery categorized to include lightbox style zoom.
▪ Contact - Contact details and connection information
• About
• Bannered header
• Content appropriately formatted to subject
• Gallery
• Bannered header
• Each of the albums would have their own categorized image content
• Contact
• Bannered header
• Social Media connector available on all pages (like box, feed, etc) if applicable
• Content can be updated on all pages
• Basic Optimization for SEO with title tags, meta data where applicable.
• Vantora Metrics and Sitemap installed. (vantora account will be provided)
• Vantora Firm Directory and Crawl Desk Accounts created

```html
<!DOCTYPE html>
<html lang="en">
<head>
<meta charset="utf-8">
<title>Tobbs Maple Grove — Landscape Construction &amp; Maintenance</title>
<link rel="stylesheet" href="https://fonts.googleapis.com/css2?family=Nunito:wght@600;700;800&family=Lato:wght@400;700&display=swap">
<style>
:root{
  --green:#77cc00;
  --green-dark:#137a2b;
  --ink:#111;
  --text:#777;
  --body:#333;
  --gray-bg:#f2f2f2;
  --black:#000;
  --white:#fff;
}
*{box-sizing:border-box;margin:0;padding:0}
html,body{width:1200px;height:3248px;overflow:hidden}
body{position:relative;font-family:"Lato",sans-serif;color:var(--body);background:var(--white)}
.abs{position:absolute}
.heading{font-family:"Nunito",sans-serif;font-weight:700;color:var(--ink)}
.eyebrow{font-family:"Nunito",sans-serif;font-weight:700;color:var(--green);font-size:19px}
.btn-leaf{display:flex;align-items:center;justify-content:center;color:var(--white);font-weight:700;font-size:15px;
  background:linear-gradient(90deg,var(--green-dark),var(--green));border-radius:40px 0 40px 0}
.photo{position:absolute}

/* hero */
.hero{position:absolute;left:0;top:0;width:1200px;height:782px;
  background:linear-gradient(180deg,#5d6a5a 0%,#7d7f62 12%,#3d5a2a 30%,#2c4a1c 55%,#1e3812 100%)}
.brand{left:142px;top:36px;font-family:"Nunito",sans-serif;font-weight:700;font-size:30px;color:var(--white)}
.topbar{left:435px;top:0;width:765px;height:48px;background:var(--white);clip-path:polygon(0 0,100% 0,100% 100%,36px 100%)}
.topbar .item{position:absolute;top:6px;display:flex;align-items:center;gap:12px;font-size:14px;color:var(--body);white-space:nowrap}
.ico{width:34px;height:34px;border-radius:50%;background:var(--green);display:flex;align-items:center;justify-content:center;flex:none}
.login{position:absolute;left:520px;top:5px;width:130px;height:35px;background:linear-gradient(90deg,var(--green-dark),var(--green));
  border-radius:20px 0 20px 0;color:#fff;font-weight:700;font-size:15px;display:flex;align-items:center;justify-content:center;gap:8px}
.navbar{left:433px;top:48px;width:767px;height:49px;background:linear-gradient(90deg,var(--green-dark),var(--green) 60%);
  clip-path:polygon(38px 0,100% 0,100% 100%,0 100%)}
.navbar ul{list-style:none;display:flex;gap:59px;position:absolute;left:80px;top:14px}
.navbar li{color:#fff;font-weight:700;font-size:15px}
.hero-welcome{left:108px;top:262px;font-family:"Nunito",sans-serif;font-weight:700;font-size:37px;color:var(--green)}
.hero-title{left:108px;top:300px;font-family:"Nunito",sans-serif;font-weight:800;font-size:60px;color:#fff}
.hero-text{left:110px;top:380px;font-size:15.5px;line-height:26px;color:#fff}
.dots span{position:absolute;left:1141px;width:11px;height:11px;border-radius:50%;background:#fff}
.dots span.hollow{background:transparent;border:1.5px solid #fff}

/* about */
.about-text{left:478px;top:850px;width:612px;font-size:15.5px;line-height:25px;color:var(--text)}

/* projects */
.projects{left:0;top:1524px;width:1200px;height:722px;background:var(--gray-bg)}
.center{left:0;width:1200px;text-align:center}

/* contact */
.info-ico{position:absolute;width:50px;height:50px;border-radius:50%;border:2px solid var(--green-dark);display:flex;align-items:center;justify-content:center}
.info-title{font-family:"Nunito",sans-serif;font-weight:700;font-size:21px;color:var(--ink)}
.info-text{font-size:15.5px;line-height:24px;color:var(--body)}
.field{position:absolute;background:#fff;box-shadow:0 2px 14px rgba(0,0,0,.07);font-size:15px;color:#888;padding:16px 24px}
.submit{position:absolute;left:436px;top:2605px;width:318px;height:52px;background:var(--green);color:#fff;font-weight:700;font-size:15px;display:flex;align-items:center;justify-content:center}

/* footer */
.footer{left:0;top:2900px;width:1200px;height:348px;background:var(--black)}
.f-title{font-family:"Nunito",sans-serif;font-weight:700;color:#fff;font-size:22px}
.f-text{color:#fff;font-size:15px;line-height:24px}
.social span{display:inline-block;width:32px;height:32px;border-radius:50%;background:#fff;margin-right:6px}
.social span.on{background:var(--green)}
.copyright a{color:var(--green);text-decoration:underline}
</style>
</head>
<body>

<!-- hero -->
<section class="hero" role="img" aria-label="Photo of a lakeside garden with wooden chairs, tall grasses, flowers and a white fence at dusk"></section>
<div class="abs brand">Tobbs Maple Grove</div>
<div class="abs topbar">
  <div class="item" style="left:64px"><span class="ico"><svg width="16" height="12" viewBox="0 0 16 12"><rect width="16" height="12" rx="1" fill="#fff"/><path d="M0 1l8 6 8-6" stroke="#77cc00" stroke-width="1.6" fill="none"/></svg></span>Tobb@TobbsMapleGrove.example</div>
  <div class="item" style="left:332px"><span class="ico"><svg width="16" height="16" viewBox="0 0 24 24"><path fill="#fff" d="M6.6 10.8a15 15 0 006.6 6.6l2.2-2.2a1 1 0 011-.25 11.4 11.4 0 003.6.57 1 1 0 011 1V20a1 1 0 01-1 1A17 17 0 013 4a1 1 0 011-1h3.5a1 1 0 011 1c0 1.25.2 2.45.57 3.57a1 1 0 01-.25 1z"/></svg></span>(555) 014-2290</div>
  <div class="login"><svg width="12" height="13" viewBox="0 0 12 13"><circle cx="6" cy="3.5" r="3.2" fill="#fff"/><path d="M0 13c0-4 2.7-5.5 6-5.5S12 9 12 13z" fill="#fff"/></svg>Login</div>
</div>
<nav class="abs navbar"><ul><li>Home</li><li>About Us</li><li>Services</li><li>Our Blog</li><li>Contact Us</li></ul></nav>
<div class="abs hero-welcome">Welcome To</div>
<h1 class="abs hero-title">Tobbs Maple Grove</h1>
<p class="abs hero-text">Lorem ipsum dolor sit amet, consectetur adipiscing elit,<br>sed do eiusmod tempor incididunt ut</p>
<div class="abs btn-leaf" style="left:110px;top:451px;width:148px;height:51px">Get Started</div>
<div class="dots"><span style="top:342px"></span><span class="hollow" style="top:365px"></span><span style="top:388px"></span><span style="top:411px"></span></div>
<svg class="abs" style="left:0;top:620px" width="1200" height="170" viewBox="0 0 1200 170">
  <defs><linearGradient id="wg" x1="0" x2="1"><stop offset="0" stop-color="#137a2b"/><stop offset=".55" stop-color="#77cc00"/><stop offset="1" stop-color="#77cc00"/></linearGradient></defs>
  <path d="M0 108 C220 170 420 130 640 80 C820 40 960 10 1200 120 L1200 170 L0 170Z" fill="url(#wg)"/>
  <path d="M0 112 C220 178 420 145 650 95 C830 58 970 40 1200 136 L1200 170 L0 170Z" fill="#137a2b"/>
  <path d="M0 114 C230 186 430 160 660 112 C840 74 980 62 1200 138 L1200 170 L0 170Z" fill="#fff"/>
</svg>

<!-- about -->
<div class="abs" style="left:114px;top:860px;width:42px;height:2px;background:var(--green)"></div>
<div class="abs eyebrow" style="left:163px;top:848px">About Us</div>
<h2 class="abs heading" style="left:113px;top:874px;font-size:52px">Who We Are</h2>
<div class="abs btn-leaf" style="left:113px;top:951px;width:166px;height:54px">Learn More</div>
<p class="abs about-text">Tobb's Maple Grove is a full service landscape construction and maintenance company. We have been servicing the community for over 20 years and in that time have established ourselves as a premier contractor in the Hamptons. We pride ourselves on quality work and excellent customer service. Lorem ipsum dolor sit amet, consectetur adipiscing elit, sed do eiusmod tempor incididunt ut labore et dolore magna aliqua. Ut enim ad minim veniam, quis nostrud exercitation ullamco</p>
<div class="photo" style="left:113px;top:1040px;width:342px;height:328px;background:linear-gradient(160deg,#c9ccc8,#3f6a2a 45%,#24481a)" role="img" aria-label="Photo of evergreen trees in front of a shingled house"></div>
<div class="photo" style="left:478px;top:1056px;width:612px;height:375px;background:linear-gradient(180deg,#b8bcbf 0%,#9aa39a 35%,#4f7a30 60%,#7d8078 80%,#4e8a2a)" role="img" aria-label="Photo of a curving driveway leading to a shingled house among trees"></div>

<!-- projects -->
<section class="abs projects"></section>
<div class="abs center eyebrow" style="top:1584px">— Our Projects —</div>
<h2 class="abs center heading" style="top:1610px;font-size:34px">Our Office Helps Services</h2>
<div class="photo" style="left:108px;top:1678px;width:486px;height:244px;background:linear-gradient(180deg,#d5d6d3,#8a8070 50%,#5a7a3a 80%,#8a8478)" role="img" aria-label="Photo of a large shingle-style house with stone walkway"></div>
<div class="photo" style="left:606px;top:1678px;width:237px;height:237px;background:linear-gradient(180deg,#c8ccc8,#4a7a2c 50%,#5c8a32)" role="img" aria-label="Photo of a stepping-stone garden path between shrubs"></div>
<div class="photo" style="left:853px;top:1678px;width:236px;height:237px;background:linear-gradient(180deg,#5a86c8,#9ab0c4 35%,#5a6048 60%,#7ab040)" role="img" aria-label="Photo of a modern house entrance with lawn pavers"></div>
<div class="photo" style="left:108px;top:1931px;width:240px;height:236px;background:linear-gradient(180deg,#7a98c0,#e0e2e4 30%,#4a6a38 65%,#8a9a70)" role="img" aria-label="Photo of ornamental grasses beside a house with timber posts"></div>
<div class="photo" style="left:358px;top:1931px;width:237px;height:236px;background:linear-gradient(180deg,#8aa8c8,#7a6a58 40%,#4a7a2a 70%,#9ab07a)" role="img" aria-label="Photo of a pergola entrance with stepping stones through grass"></div>
<div class="photo" style="left:605px;top:1922px;width:485px;height:245px;background:linear-gradient(180deg,#c8cccc,#a89078 35%,#2f6a22 60%,#3f7a2a)" role="img" aria-label="Photo of a formal boxwood garden before a villa"></div>

<!-- contact -->
<div class="abs center eyebrow" style="top:2301px">— Get a Quote —</div>
<h2 class="abs center heading" style="top:2327px;font-size:34px">Contact Us</h2>

<div class="info-ico" style="left:113px;top:2399px"><svg width="12" height="16" viewBox="0 0 12 16"><path d="M6 0a6 6 0 00-6 6c0 4.5 6 10 6 10s6-5.5 6-10a6 6 0 00-6-6z" fill="#137a2b"/><circle cx="6" cy="6" r="2.2" fill="#fff"/></svg></div>
<div class="abs" style="left:178px;top:2397px"><div class="info-title">Location</div><div class="info-text">P.O. Box 318<br>Alder Hollow, NY 10990</div></div>
<div class="info-ico" style="left:113px;top:2503px"><svg width="16" height="16" viewBox="0 0 24 24"><path fill="#137a2b" d="M6.6 10.8a15 15 0 006.6 6.6l2.2-2.2a1 1 0 011-.25 11.4 11.4 0 003.6.57 1 1 0 011 1V20a1 1 0 01-1 1A17 17 0 013 4a1 1 0 011-1h3.5a1 1 0 011 1c0 1.25.2 2.45.57 3.57a1 1 0 01-.25 1z"/></svg></div>
<div class="abs" style="left:178px;top:2503px"><div class="info-title">Phone</div><div class="info-text">(555) 014-2290</div></div>
<div class="info-ico" style="left:113px;top:2599px"><svg width="15" height="11" viewBox="0 0 16 12"><rect width="16" height="12" rx="1" fill="#137a2b"/><path d="M0 1l8 6 8-6" stroke="#fff" stroke-width="1.6" fill="none"/></svg></div>
<div class="abs" style="left:178px;top:2598px"><div class="info-title">Email</div><div class="info-text">Tobb@TobbsMapleGrove.example</div></div>

<div class="field" style="left:436px;top:2400px;width:318px;height:53px">Name</div>
<div class="field" style="left:436px;top:2468px;width:318px;height:53px">Phone</div>
<div class="field" style="left:436px;top:2536px;width:318px;height:53px">Email</div>
<div class="submit">Submit</div>
<div class="field" style="left:774px;top:2400px;width:301px;height:257px">Type your message</div>

<!-- footer -->
<footer class="abs footer"></footer>
<svg class="abs" style="left:0;top:2720px" width="1200" height="200" viewBox="0 0 1200 200">
  <path d="M0 20 C150 90 300 150 470 140 C670 125 850 30 1040 22 C1120 20 1170 30 1200 40 L1200 200 L0 200Z" fill="#77cc00"/>
  <path d="M0 58 C170 140 330 178 500 165 C640 152 760 105 880 70 L1200 70 L1200 200 L0 200Z" fill="#137a2b"/>
  <path d="M0 72 C180 160 340 190 520 180 C700 168 860 80 1040 30 C1110 28 1170 48 1200 70 L1200 200 L0 200Z" fill="#000"/>
  <path d="M1000 22 C1080 18 1150 22 1200 40 L1200 0 L1060 0Z" fill="#fff"/>
  <path d="M1030 24 C1110 14 1170 30 1200 48 L1200 200 L1100 200Z" fill="#000"/>
</svg>
<div class="abs f-title" style="left:110px;top:2942px;font-size:31px">Tobbs Maple Grove</div>
<p class="abs f-text" style="left:111px;top:2998px;width:280px">Lorem ipsum dolor sit amet, consectetur adipiscing elit, sed do eiusmod tempor incididunt ut labore et dolore magna aliqua.</p>

<div class="abs f-title" style="left:432px;top:2940px">Contact Us</div>
<div class="abs f-text" style="left:434px;top:2982px">
  <div style="display:flex;gap:10px"><svg width="11" height="15" viewBox="0 0 12 16" style="margin-top:4px"><path d="M6 0a6 6 0 00-6 6c0 4.5 6 10 6 10s6-5.5 6-10a6 6 0 00-6-6z" fill="#fff"/><circle cx="6" cy="6" r="2.2" fill="#000"/></svg><div>P.O. Box 318<br>Alder Hollow, NY 10990</div></div>
  <div style="display:flex;gap:10px;margin-top:14px"><svg width="13" height="13" viewBox="0 0 24 24" style="margin-top:5px"><path fill="#fff" d="M6.6 10.8a15 15 0 006.6 6.6l2.2-2.2a1 1 0 011-.25 11.4 11.4 0 003.6.57 1 1 0 011 1V20a1 1 0 01-1 1A17 17 0 013 4a1 1 0 011-1h3.5a1 1 0 011 1c0 1.25.2 2.45.57 3.57a1 1 0 01-.25 1z"/></svg>(555) 014-2290</div>
  <div style="display:flex;gap:10px;margin-top:14px"><svg width="15" height="11" viewBox="0 0 16 12" style="margin-top:7px"><rect width="16" height="12" rx="1" fill="#fff"/><path d="M0 1l8 6 8-6" stroke="#000" stroke-width="1.6" fill="none"/></svg>Tobb@TobbsMapleGrove.example</div>
</div>

<div class="abs f-title" style="left:718px;top:2940px">Support</div>
<div class="abs f-text" style="left:720px;top:2984px;line-height:30px">Terms &amp; Conditions<br>Contact us<br>Privacy Policy</div>

<div class="abs f-title" style="left:930px;top:2940px">Follow Us</div>
<div class="abs social" style="left:930px;top:2982px"><span class="on"></span><span></span><span></span><span></span></div>

<div class="abs" style="left:110px;top:3160px;width:980px;height:1px;background:#333"></div>
<div class="abs center f-text copyright" style="top:3188px">©Copyrights 2022 <a>Tobbs Maple Grove</a> &nbsp;|&nbsp;&nbsp; All Rights Reserved</div>

</body>
</html>
```